Business card for Quorvane, LLC

I need a business card template in .ai or similar format for my IT consultancy, Quorvane(.com)

Front side: The usual name/title/number/fax/email/contact info. Definitely san-serif, the logo font is MuseoSans 500 so the company name (Quorvane, LLC.) should definitely be in the same type and the rest of the text should be that or something complimentary. Including logo on the front is optional - I would prefer designs that include both with and without. I am open to creative input on the format.

Back side: Company logo framed somehow. I was thinking red background with the logo in a white circle in the middle, tho' I'm not sure how that would play off the red ball in the elephant's trunk. Open to creative input here too.

Attached are a (very rough) one-sided card mock-up I made, along with the logo and logo font.

```html
<!DOCTYPE html>
<html lang="en">
<head>
<meta charset="utf-8">
<title>Quorvane, LLC — Business Card</title>
<link rel="stylesheet" href="https://fonts.googleapis.com/css2?family=Mulish:wght@400;500;800&display=swap">
<style>
  :root {
    --stage: #e9e9e9;
    --card-white: #ffffff;
    --card-dark: #48484a;
    --brand-red: #e3202a;
    --ink-dark: #3a3a3c;
    --ink-light: #f2f2f2;
    --ink-muted: #b9b9bb;
    --shadow: rgba(0, 0, 0, 0.22);
  }
  * { box-sizing: border-box; margin: 0; padding: 0; }
  html, body {
    width: 1200px;
    height: 748px;
    overflow: hidden;
    background: var(--stage);
    font-family: "Mulish", sans-serif;
  }
  .sheet {
    width: 1200px;
    height: 748px;
    display: flex;
    align-items: center;
    justify-content: center;
    gap: 40px;
  }
  .card {
    position: relative;
    width: 540px;
    height: 310px;
    box-shadow: 0 6px 18px var(--shadow);
    overflow: hidden;
  }

  /* Back side */
  .card--back {
    background: var(--card-white);
    display: flex;
    flex-direction: column;
    align-items: center;
    justify-content: center;
  }
  .brand {
    display: flex;
    align-items: center;
    gap: 10px;
  }
  .brand__dot {
    width: 22px;
    height: 22px;
    border-radius: 50%;
    background: var(--brand-red);
  }
  .brand__name {
    color: var(--brand-red);
    font-weight: 800;
    font-size: 34px;
    letter-spacing: 0.5px;
  }
  .card--back .web {
    margin-top: 26px;
    font-size: 12px;
    color: var(--ink-dark);
    letter-spacing: 0.3px;
  }

  /* Front side */
  .card--front {
    background: var(--card-dark);
  }
  .card--front .brand {
    position: absolute;
    left: 34px;
    top: 178px;
    gap: 7px;
  }
  .card--front .brand__dot { width: 12px; height: 12px; }
  .card--front .brand__name { font-size: 16px; }
  .accent-dot {
    position: absolute;
    right: 92px;
    top: 44px;
    width: 26px;
    height: 26px;
    border-radius: 50%;
    background: var(--brand-red);
  }
  .contact {
    position: absolute;
    left: 212px;
    top: 128px;
    color: var(--ink-light);
  }
  .contact__name {
    font-size: 20px;
    font-weight: 500;
    letter-spacing: 0.3px;
  }
  .contact__title {
    font-size: 11px;
    color: var(--brand-red);
    margin: 2px 0 6px;
  }
  .contact__line {
    font-size: 11px;
    line-height: 16px;
    letter-spacing: 0.2px;
  }
  .initials {
    position: absolute;
    right: 70px;
    bottom: 14px;
    font-size: 11px;
    color: var(--ink-muted);
    letter-spacing: 1px;
  }
</style>
</head>
<body>
<main class="sheet">
  <section class="card card--back" aria-label="Card back">
    <div class="brand">
      <span class="brand__dot"></span>
      <span class="brand__name">QUORVANE</span>
    </div>
    <p class="web">www.quorvane.com</p>
  </section>

  <section class="card card--front" aria-label="Card front">
    <span class="accent-dot"></span>
    <div class="brand">
      <span class="brand__dot"></span>
      <span class="brand__name">QUORVANE</span>
    </div>
    <div class="contact">
      <p class="contact__name">Dana Kessler</p>
      <p class="contact__title">President, Founder</p>
      <p class="contact__line">18 Harrow Ln. Fernvale, PA 19077-2140</p>
      <p class="contact__line">Email: dkessler@quorvane.com</p>
      <p class="contact__line">Phone: 1.800.555.0142</p>
      <p class="contact__line">Mobile: 1.215.555.0187</p>
      <p class="contact__line">Fax: 1.215.555.0163</p>
    </div>
    <span class="initials">DK</span>
  </section>
</main>
</body>
</html>
```